Energy cost saving website (job description rewritten!)

Job Type: WordPress design
Task Outline: Create a WordPress design
Task Description:
We are new business (Germany) in the market of saving costs by power-saving (name: 'uns-gefaellt-der-Ruhetag.de'). This is reached by changing the supplier, the use of LED bulbs, energy saving washing machines, stoves, microwaves, hairdryers, vacuum cleaners and the like - where all of these be selled or affiliated through the website maybe you will create for us.
Design parameters:
We want a serious design that embodies a feeling of honesty, competence and capability.
Visitors should particularly see that this site saves them money!
The home page mainly should act as a selector of possibilities saving money by power-saving, usage of LED bulbs and large energy saving household devices (washing machines, etc.)
Updates
Hello designers,
browsing through the PixelHarbors files of portfolios I found one header graphics which excites me. Please find it here: http://www.pixelharbor-example.com/design/482613/wordpress-design-by-tarun-mehlvi . Note: it is NOT the picture but the shadowing. So if you consider this in your concepts would be another 'nice-to-have'.
Thanks.
Reason: Give more time for newly invited disigners to submit designs.
Reason: Some designs still unter contruction.
Target Market(s)
People looking out for saving money by power-saving.
Industry/Entity Type
Business
Requirements
Must have
- Look and feel of 'this site saves me money'!
Nice to have
- We love 3D effects, but its not a must have. We also like cartoons, but feel free to develop your own concept, please. An appropriate backgrond picture would be nice.
Should not have
- Some kind of these exaggerated smiling or handshaking photos. That bathetic symbols like money bills or coins stacks.

```html
<!DOCTYPE html>
<html lang="en">
<head>
<meta charset="utf-8">
<title>uns-gefaellt-der-Ruhetag.de</title>
<link rel="stylesheet" href="https://fonts.googleapis.com/css2?family=PT+Sans+Narrow:wght@400;700&family=Noto+Sans:wght@400&display=swap">
<style>
:root{
  --page:#f4f4f4;
  --white:#ffffff;
  --teal:#5fc4cf;
  --teal-dark:#3aa3b0;
  --teal-band-top:#8fd8df;
  --teal-band-bottom:#3ea8b4;
  --text:#555555;
  --nav:#555555;
  --lime:#a6c23c;
  --lime-dark:#8caa28;
  --footer:#444444;
  --line:#e2e2e2;
}
*{margin:0;padding:0;box-sizing:border-box}
html,body{width:1200px;height:1130px;overflow:hidden;background:var(--page)}
body{position:relative;font-family:"Noto Sans",Verdana,sans-serif;color:var(--text)}
.abs{position:absolute}
.teal-band{left:0;top:163px;width:1200px;height:340px;background:linear-gradient(180deg,var(--teal-band-top),var(--teal-band-bottom))}
.header-box{left:174px;top:22px;width:854px;height:631px;background:var(--white);border:1px solid var(--line)}
.header-top{left:175px;top:23px;width:852px;height:140px;background:linear-gradient(180deg,#fff,#f6f6f6)}
.logo{left:198px;top:54px;display:flex;align-items:center;gap:10px}
.logo-mark{width:36px;height:36px;border-radius:50%;background:var(--teal)}
.logo-name{font-family:"PT Sans Narrow",sans-serif;font-weight:700;font-size:22px;letter-spacing:.5px;color:var(--teal);text-transform:uppercase;line-height:1}
.nav{left:181px;top:124px;height:39px;display:flex;font-family:"PT Sans Narrow",sans-serif;font-size:15px;letter-spacing:.8px;text-transform:uppercase;color:var(--nav)}
.nav a{color:inherit;text-decoration:none;display:flex;align-items:center;height:39px;padding-top:8px}
.nav .active{background:var(--white);color:var(--teal);padding:8px 18px 0;border:1px solid #eee;border-bottom:none}
.hero-shadow{left:190px;top:480px;width:820px;height:50px;border-radius:50%;background:radial-gradient(ellipse at center,rgba(0,0,0,.55),rgba(0,0,0,0) 70%)}
.hero{left:181px;top:163px;width:839px;height:334px;border:4px solid rgba(255,255,255,.6);
  background:linear-gradient(100deg,#c9d3c6 0%,#8d8a7f 30%,#5b544b 55%,#8a7666 80%,#c9a58f 100%)}
.hero-box{left:702px;top:179px;width:300px;height:296px;background:rgba(70,70,70,.82);padding:14px 22px}
.hero-title{font-family:"PT Sans Narrow",sans-serif;font-weight:700;font-size:47px;line-height:55px;color:#fff;text-transform:uppercase}
.hero-title span{color:var(--teal)}
.hero-text{margin-top:12px;font-size:11px;line-height:19px;color:#fff;letter-spacing:.2px}
.hero-text span{color:var(--teal)}
.intro{left:214px;top:530px}
.intro h2{font-family:"PT Sans Narrow",sans-serif;font-weight:400;font-size:14px;letter-spacing:.8px;color:var(--teal-dark);text-transform:uppercase;margin-left:3px}
.intro p{margin-top:10px;width:470px;font-size:11px;line-height:22.5px;letter-spacing:.3px}
.cta{left:750px;width:222px;height:46px;border:1px solid var(--lime-dark);border-radius:2px;background:linear-gradient(180deg,#b9d24f,var(--lime));
  color:#fff;font-family:"PT Sans Narrow",sans-serif;font-weight:700;font-size:17px;letter-spacing:.8px;text-transform:uppercase;display:flex;align-items:center;justify-content:center;box-shadow:0 0 0 2px #e9f0cf inset}
.cta-save{top:526px}
.cta-info{top:584px}
.features-box{left:174px;top:663px;width:854px;height:365px;background:var(--white);border:1px solid var(--line)}
.card{top:691px;width:248px;height:309px;background:var(--white);border:1px solid #e4e4e4;border-radius:4px;box-shadow:0 1px 3px rgba(0,0,0,.08);overflow:hidden}
.card-head{height:38px;background:#f2f2f2;display:flex;align-items:center;gap:10px;padding-left:18px;font-family:"PT Sans Narrow",sans-serif;font-size:14px;letter-spacing:.8px;color:var(--teal);text-transform:uppercase}
.card-head svg{width:22px;height:22px}
.card p{padding:12px 16px 0;font-size:11px;line-height:19px;letter-spacing:.2px;height:96px}
.card-photo{height:125px;background:linear-gradient(100deg,#dadfd9 0%,#f2f2f2 40%,#e8ddd2 70%,#c79a6a 100%)}
.more{display:block;margin:10px auto 0;width:70px;height:30px;background:linear-gradient(180deg,#6ccbd5,var(--teal-dark));border:1px solid #2f8f9b;color:#fff;font-family:"PT Sans Narrow",sans-serif;font-size:15px;letter-spacing:.8px;text-align:center;line-height:28px}
.footer{left:174px;top:1072px;width:854px;height:58px;background:var(--footer);display:flex;align-items:center;justify-content:space-between;padding:0 27px;font-size:8.5px;color:#ccc}
.footer nav{display:flex;gap:15px}
.footer .active{color:var(--teal)}
</style>
</head>
<body>
<div class="abs teal-band"></div>
<div class="abs header-box"></div>
<div class="abs header-top"></div>

<div class="abs logo">
  <div class="logo-mark"></div>
  <div class="logo-name">uns-gefaellt-der-Ruhetag.de</div>
</div>

<nav class="abs nav">
  <a class="active">Home</a>
  <a style="margin-left:32px">How we can save you money</a>
  <a style="margin-left:52px">Calculate your savings</a>
  <a style="margin-left:47px">Testimonials</a>
  <a style="margin-left:52px">Blog</a>
  <a style="margin-left:48px">Get in touch</a>
</nav>

<div class="abs hero-shadow"></div>
<div class="abs hero" role="img" aria-label="Photo of a smiling woman in a green top holding an energy-saving bulb in a blurred living room"></div>
<div class="abs hero-box">
  <h1 class="hero-title">We help to<br>reduce your<br><span>power costs</span></h1>
  <p class="hero-text">We are new business in the market of saving costs by power-saving This is reached by changing the supplier, the use of <span>LED bulbs, energy saving washing machines, stoves, micro-waves, hairdryers, vacuum cleaners</span></p>
</div>

<section class="abs intro">
  <h2>Headline one will go here</h2>
  <p>Cras vel velit mauris. Proin et odio eu dui euismod congue eget et neque. Maecenas lectus magna, dignissim et varius vitae, venenatis vitae magna. Suspendisse lobortis tincidunt fringilla erretunting.</p>
</section>
<a class="abs cta cta-save">Start saving money</a>
<a class="abs cta cta-info">Sign up for more info</a>

<div class="abs features-box"></div>

<article class="abs card" style="left:201px">
  <div class="card-head">
    <svg viewBox="0 0 24 24" fill="none" stroke="#555" stroke-width="2" stroke-linecap="round"><path d="M9 9l6 6M7 11l6 6-2 2a4 4 0 0 1-6-6zM13 7l4 4 2-2a3 3 0 0 0-4-4zM4 20l3-3M17 7l3-3"/></svg>
    Change electric provider
  </div>
  <p>Cras vel velit mauris. Proin et odio eu dui euismod congue eget et neque. Maecenas lectus magna, dignissim et varius vitae heetore.</p>
  <div class="card-photo" role="img" aria-label="Photo of a technician and a customer signing a form"></div>
  <a class="more">MORE</a>
</article>

<article class="abs card" style="left:477px">
  <div class="card-head">
    <svg viewBox="0 0 24 24" fill="none" stroke="#555" stroke-width="2" stroke-linecap="round"><path d="M12 2a6 6 0 0 0-4 10.5c1 1 1.5 2 1.5 3.5h5c0-1.5.5-2.5 1.5-3.5A6 6 0 0 0 12 2zM9.5 19h5M10.5 22h3"/></svg>
    Change to LED bulbs
  </div>
  <p>Cras vel velit mauris. Proin et odio eu dui euismod congue eget et neque. Maecenas lectus magna, dignissim et varius vitae heetore.</p>
  <div class="card-photo" role="img" aria-label="Photo of a technician and a customer signing a form"></div>
  <a class="more">MORE</a>
</article>

<article class="abs card" style="left:751px">
  <div class="card-head">
    <svg viewBox="0 0 24 24" fill="#555"><rect x="7" y="3" width="8" height="2"/><rect x="10" y="5" width="2" height="3"/><path d="M3 9h13a4 4 0 0 1 4 4v2h-3v-2a1 1 0 0 0-1-1H3z"/><path d="M18.5 17c1 1.5 1.5 2.3 1.5 3a1.5 1.5 0 0 1-3 0c0-.7.5-1.5 1.5-3z"/></svg>
    Household appliances
  </div>
  <p>Cras vel velit mauris. Proin et odio eu dui euismod congue eget et neque. Maecenas lectus magna, dignissim et varius vitae heetore.</p>
  <div class="card-photo" role="img" aria-label="Photo of a technician and a customer signing a form"></div>
  <a class="more">MORE</a>
</article>

<footer class="abs footer">
  <nav><span class="active">home</span><span>save money</span><span>calculate your savings</span><span>testimonials</span><span>blog</span><span>get in touch</span></nav>
  <span>copyright 2012</span>
</footer>
</body>
</html>
```